依頼詳細
サイズが決まっています。添付データのサイズを参照してください。
モルテナカタログのような感じのデザインをお願いします。
記載項目
日常生活に支援が必要な方、支援をする方へ『あんしん』をお届けします。

使いやすい、見やすい、分かりやすい
希望イメージ
シンプル 複雑
単色 カラフル
暗い 明るい
日常 高級
遊び心 厳粛
未来的 伝統的
女性的 男性的
希望する色
青系、緑系
納品ファイル
• イラストレーター形式 (.ai)
補足説明
”カタログの表紙を別刷り”というのは
添付したSOFT ROAD の下のオレンジの枠内を差し替えるということです。
依頼内容が分かりにくいようで失礼いたしました。
■ 選んだ理由

今回、当カタログの取り扱い品目と安心を届けるというコンセプトに合致している点、そして社内での投票をさせて頂きました結果、korumi様のご提案を採用させて戴きました。

■ 提案者全員のお礼・コメント

今度は本当に沢山のご提案をいただきまして有難うございました。
どのランサーの方の提案も素晴らしいものばかりでしたが、
上記理由により、社内で最も票の多かった提案を採用させて頂きました。

```html
<!DOCTYPE html>
<html lang="ja">
<head>
<meta charset="utf-8">
<title>SOFT ROAD 福祉用具総合カタログ vol.32</title>
<link rel="stylesheet" href="https://fonts.googleapis.com/css2?family=Noto+Sans+JP:wght@500;700;900&family=Noto+Serif+JP:wght@700;900&family=Oswald:wght@500&display=swap">
<style>
  :root {
    --paper: #ffffff;
    --title-red: #e5344f;
    --label-green: #4aa23a;
    --sky-top: #3f9be0;
    --sky-low: #d9effa;
    --grass-top: #9bd35a;
    --grass-low: #5aa632;
    --badge-green: #7bc043;
    --ink: #2b2b2b;
    --white: #ffffff;
  }
  * { margin: 0; padding: 0; box-sizing: border-box; }
  html, body { width: 851px; height: 1200px; overflow: hidden; background: var(--paper); }
  .cover {
    position: relative;
    width: 851px;
    height: 1200px;
    background: var(--paper);
    font-family: "Noto Sans JP", sans-serif;
    overflow: hidden;
  }
  .masthead { position: absolute; top: 0; left: 0; width: 100%; height: 255px; text-align: center; }
  .catalog-label {
    position: absolute; top: 36px; width: 100%;
    font-size: 24px; font-weight: 700; color: var(--label-green); letter-spacing: 2px;
  }
  .catalog-title {
    position: absolute; top: 78px; width: 100%;
    font-family: "Oswald", sans-serif; font-weight: 500;
    font-size: 136px; line-height: 1; color: var(--title-red); letter-spacing: 10px;
  }
  .tagline {
    position: absolute; top: 228px; width: 100%;
    font-family: "Oswald", sans-serif; font-size: 14px; color: var(--ink); letter-spacing: 1px;
  }
  .scene {
    position: absolute; top: 255px; left: 0; width: 100%; height: 860px;
    background: linear-gradient(180deg, var(--sky-top) 0%, var(--sky-low) 43%, var(--grass-top) 46%, var(--grass-low) 100%);
  }
  .characters {
    position: absolute; left: 100px; top: 630px; width: 630px; height: 485px;
    border-radius: 40px;
    background: radial-gradient(ellipse at 50% 55%, rgba(255,255,255,0.3), rgba(255,255,255,0) 70%);
  }
  .message {
    position: absolute; left: 0; top: 0; width: 100%;
    color: var(--white); font-family: "Noto Serif JP", serif; font-weight: 700;
    text-shadow: 0 1px 3px rgba(0,60,110,0.35);
  }
  .message .line { position: absolute; white-space: nowrap; font-size: 31px; line-height: 1.2; }
  .message .line-1 { left: 163px; top: 274px; }
  .message .line-2 { left: 163px; top: 326px; }
  .message .line-3 { left: 136px; top: 378px; }
  .message .key { font-size: 58px; font-weight: 900; }
  .volume {
    position: absolute; left: 660px; top: 286px;
    font-family: "Oswald", sans-serif; font-size: 42px; line-height: 1; color: var(--white);
  }
  .badge {
    position: absolute; width: 102px; height: 102px; border-radius: 50%;
    background: var(--badge-green); color: var(--white);
    display: flex; align-items: center; justify-content: center; text-align: center;
    font-size: 23px; font-weight: 900; line-height: 1.15;
    box-shadow: 0 3px 6px rgba(0,0,0,0.15);
  }
  .badge-use { left: 375px; top: 607px; }
  .badge-see { left: 494px; top: 579px; }
  .badge-know { left: 624px; top: 517px; }
  .publisher {
    position: absolute; bottom: 0; left: 0; width: 100%; height: 85px;
    background: var(--paper);
    display: flex; align-items: center; justify-content: center; gap: 14px;
  }
  .publisher-mark { width: 30px; height: 30px; border-radius: 50%; background: var(--ink); }
  .publisher-name { font-size: 30px; font-weight: 500; color: var(--ink); letter-spacing: 2px; }
</style>
</head>
<body>
<main class="cover">
  <header class="masthead">
    <p class="catalog-label">福祉用具総合カタログ</p>
    <h1 class="catalog-title">SOFT ROAD</h1>
    <p class="tagline">FOR GOOD HAPPINESS HUMAN LIFE</p>
  </header>

  <section class="scene" role="img" aria-label="青空と芝生の背景"></section>
  <div class="characters" role="img" aria-label="芝生の上のハート型の車椅子と、手をつなぐ笑顔の老夫婦の指人形"></div>

  <div class="message">
    <span class="line line-1">日常生活に支援が必要な方、</span>
    <span class="line line-2">支援をする方へ、</span>
    <span class="line line-3"><span class="key">『あんしん』</span>をお届けします。</span>
  </div>
  <p class="volume">vol.32</p>

  <div class="badge badge-use">使い<br>やすい</div>
  <div class="badge badge-see">見や<br>すい</div>
  <div class="badge badge-know">分かり<br>やすい</div>

  <footer class="publisher">
    <span class="publisher-mark"></span>
    <span class="publisher-name">青葉医療器株式会社</span>
  </footer>
</main>
</body>
</html>
```